I need the Scorecard I've developed for my staff to be produced into a visually engaging piece that will encourage the staff to utilize it on a daily basis. I'm thinking it could be 5x7 in size so that it isn't too cumbersome, but I'm open to different layouts.
I have multiple other departments that will need Scorecards created for them as well, but each one will contain task specific questions for each department.

```html
<!DOCTYPE html>
<html lang="en">
<head>
<meta charset="utf-8">
<title>Receptionist Daily Excellence Scorecard</title>
<link rel="stylesheet" href="https://fonts.googleapis.com/css2?family=Lora:wght@400;600;700&family=Open+Sans:ital,wght@0,400;0,600;0,700;1,400&display=swap">
<style>
:root{
  --bg:#d1d2d4;
  --paper:#ffffff;
  --accent:#ec6a2c;
  --ink:#111111;
  --header:#6d6e71;
  --line:#222222;
  --green:#3bb54a;
  --amber:#f7941d;
  --red:#c8202f;
}
*{box-sizing:border-box;margin:0;padding:0}
html,body{width:1200px;height:2799px;overflow:hidden;background:var(--bg)}
body{position:relative;font-family:"Open Sans",Arial,sans-serif;color:var(--ink)}
.page{position:absolute;left:148px;width:906px;background:var(--paper);box-shadow:10px 14px 18px rgba(0,0,0,.28)}
.page-one{top:78px;height:1269px;padding:48px 45px 0 45px}
.page-two{top:1411px;height:1269px}
.title{font-family:"Lora",Georgia,serif;font-weight:700;color:var(--accent);font-size:30px;text-align:center;letter-spacing:.3px}
.identity{display:flex;justify-content:space-between;margin-top:16px;padding-left:12px}
.fields{font-weight:600;font-size:19px;line-height:30px}
.field{display:flex;align-items:flex-end}
.field-label{width:90px}
.field-line{width:340px;border-bottom:2px solid var(--line);height:22px;margin-left:4px}
.legend{font-style:italic;font-size:19px;line-height:22.5px;width:330px;margin-top:-2px}
.section-title{font-family:"Lora",Georgia,serif;font-weight:600;color:var(--accent);font-size:22.5px;line-height:30px;height:30px}
.page-one .section-title{margin-top:14px;margin-bottom:2px}
.page-one .identity + .section-title{margin-top:18px}
.task-table{width:815px;border:2px solid var(--line)}
.task-head{display:grid;grid-template-columns:415px 152px 1fr;background:var(--header);color:#fff;font-weight:600;font-size:19px;height:30px;line-height:30px;text-align:center}
.task-head span:nth-child(2),.task-head span:nth-child(3){padding-top:3px}
.task-list{list-style:none;padding:0 0 2px 8px;font-size:19.5px;line-height:30.3px}
.task-list li::before{content:"•";margin-right:9px}
.block{position:absolute;left:45px;width:815px}
.status-list{list-style:none;font-size:19.5px;line-height:32.6px}
.status-list li{display:flex;align-items:center}
.dot{width:17px;height:17px;border-radius:50%;margin:0 15px 0 3px;flex:none}
.dot-green{background:var(--green)}.dot-amber{background:var(--amber)}.dot-red{background:var(--red)}
.write-row{display:flex;align-items:flex-end;font-size:19.5px;line-height:24px;height:27px}
.write-row .fill{flex:1;border-bottom:1.5px solid var(--line);margin-left:6px;height:20px;margin-bottom:4px}
.write-line{border-bottom:1.5px solid var(--line);height:27px}
.icon{flex:none;margin-right:8px;margin-bottom:2px}
.sub{font-style:italic;font-size:19.5px}
.rating-box{width:338px;height:134px;border:2px solid var(--line);padding:8px 11px;font-size:19.5px}
.sig-label{font-weight:600;font-size:19.5px}
.sig-line{width:248px;border-bottom:1.5px solid var(--line)}
</style>
</head>
<body>

<section class="page page-one">
  <h1 class="title">RECEPTIONIST DAILY EXCELLENCE SCORECARD</h1>
  <div class="identity">
    <div class="fields">
      <div class="field"><span class="field-label">Name</span>:<span class="field-line"></span></div>
      <div class="field"><span class="field-label">Date</span>:<span class="field-line"></span></div>
      <div class="field"><span class="field-label">Location</span>:<span class="field-line"></span></div>
    </div>
    <p class="legend">Please rate yourself for each task:<br>1 = Needs Improvement<br>3 = Meets Expectations<br>5 = Excellent</p>
  </div>

  <h2 class="section-title">1. Call Handling &amp; First Call Intake</h2>
  <div class="task-table">
    <div class="task-head"><span>Task</span><span>Self-Rating (1-5)</span><span>Notes / Issues</span></div>
    <ul class="task-list">
      <li>Answered 90%+ calls within 3 rings</li>
      <li>Maintained empathy and professionalism</li>
      <li>Accurately completed all First Call fields</li>
      <li>Worked within Receptionist role</li>
    </ul>
  </div>

  <h2 class="section-title">2. Call Management During Busy Times</h2>
  <div class="task-table">
    <div class="task-head"><span>Task</span><span>Self-Rating (1-5)</span><span>Notes / Issues</span></div>
    <ul class="task-list">
      <li>Prioritized urgent vs. non-urgent calls</li>
      <li>Hold times under 1 minute</li>
      <li>Logged all calls</li>
      <li>Requested help if overwhelmed</li>
    </ul>
  </div>

  <h2 class="section-title">3. Scheduling Accuracy</h2>
  <div class="task-table">
    <div class="task-head"><span>Task</span><span>Self-Rating (1-5)</span><span>Notes / Issues</span></div>
    <ul class="task-list">
      <li>Updated scheduling board</li>
      <li>Cross-checked with Red Book</li>
      <li>Entered manifold info promptly</li>
    </ul>
  </div>

  <h2 class="section-title">4. Clothing &amp; Flowers</h2>
  <div class="task-table">
    <div class="task-head"><span>Task</span><span>Self-Rating (1-5)</span><span>Notes / Issues</span></div>
    <ul class="task-list">
      <li>Clothing sheet completed</li>
      <li>Family contact noted on sheet</li>
      <li>Floral deliveries logged</li>
      <li>Concerns communicated to Care Center</li>
      <li>Flower placement verified</li>
    </ul>
  </div>

  <h2 class="section-title">5. Death Certificates</h2>
  <div class="task-table">
    <div class="task-head"><span>Task</span><span>Self-Rating (1-5)</span><span>Notes / Issues</span></div>
    <ul class="task-list">
      <li>Verified recipient ID &amp; relationship</li>
      <li>Confirmed correct documents enclosed</li>
      <li>Recipient signed the DC logbook</li>
      <li>Suggested proofreading before leaving</li>
    </ul>
  </div>
</section>

<section class="page page-two">
  <div class="block" style="top:48px">
    <h2 class="section-title">6. Routing &amp; Messages</h2>
    <div class="task-table" style="margin-top:2px">
      <div class="task-head"><span>Task</span><span>Self-Rating (1-5)</span><span>Notes / Issues</span></div>
      <ul class="task-list">
        <li>Calls routed appropriately</li>
        <li>Messages included all required info</li>
        <li>Delivered 95%+ messages in 30 min</li>
      </ul>
    </div>
  </div>

  <div class="block" style="top:231px">
    <h2 class="section-title">Daily Status Summary (Circle One)</h2>
    <ul class="status-list">
      <li><span class="dot dot-green"></span>Excellent – All key duties completed, proactive, calm under pressure</li>
      <li><span class="dot dot-amber"></span>Satisfactory – Most duties completed, minor follow-up needed</li>
      <li><span class="dot dot-red"></span>Needs Support – Missed urgent duties, accuracy or stress issues</li>
    </ul>
  </div>

  <div class="block" style="top:384px">
    <h2 class="section-title">Daily Reflection</h2>
    <div class="write-row">What went well today :<span class="fill"></span></div>
    <div class="write-line"></div>
    <div class="write-row">Any issues or barriers to note :<span class="fill"></span></div>
    <div class="write-line"></div>
    <div class="write-row">Support needed from supervisor :<span class="fill"></span></div>
    <div class="write-line"></div>
  </div>

  <div class="block" style="top:603px">
    <h2 class="section-title">Stars &amp; Flags (Supervisor Use Only)</h2>
    <div class="write-row">
      <svg class="icon" width="24" height="23" viewBox="0 0 24 23" aria-hidden="true"><polygon points="12,0 15,8.5 24,8.7 16.8,14 19.4,23 12,17.7 4.6,23 7.2,14 0,8.7 9,8.5" fill="#f7941d"/></svg>
      Stars (Excellence or above-and-beyond moments):<span class="fill"></span>
    </div>
    <div class="write-line"></div>
    <div class="write-line"></div>
    <div class="write-row">
      <svg class="icon" width="24" height="26" viewBox="0 0 24 26" aria-hidden="true"><rect x="1" y="0" width="2.5" height="26" fill="#222"/><polygon points="3.5,0 23,8.5 3.5,17" fill="#c8202f"/></svg>
      Flags (Concerns needing follow-up/coaching):<span class="fill"></span>
    </div>
    <div class="write-line"></div>
    <div class="write-line"></div>
  </div>

  <div class="block" style="top:821px">
    <h2 class="section-title">Manager's Overall Rating</h2>
    <p class="sub">(Please rate overall performance on a 1-5 scale)</p>
    <div class="rating-box" style="margin-top:8px">Manager Overall Rating (1-5):</div>
  </div>

  <div class="block" style="top:1058px;left:91px;width:720px">
    <div style="position:absolute;left:477px;top:0;display:flex;align-items:flex-end" class="sig-label">Date:<span style="width:190px;border-bottom:1.5px solid #222;margin-left:7px;height:18px"></span></div>
    <p class="sig-label" style="position:absolute;left:0;top:27px">Receptionist Signature:</p>
    <p class="sig-label" style="position:absolute;left:477px;top:27px">Supervisor Signature:</p>
    <div class="sig-line" style="position:absolute;left:0;top:139px"></div>
    <div class="sig-line" style="position:absolute;left:477px;top:139px"></div>
  </div>
</section>

</body>
</html>
```